Political Association Member Newsletter

We require a professional newsletter designed that will be sent both by mail and by email (and can be posted online) to the members in our client organization. I will develop and curate the content to send to the designer but we need help with a good design.

We have two key colours: red and blue (usually on white background). The pantones are:
blue = 301C
red = 032C

The logo I have from the client is attached as well as a recent piece with contact information and social media channels noted.

The client also provided a campaign logo "Raise the Bar for 2019" that will accompany copy for membership and donation which will follow.

Two preliminary content pieces are also included here: a flyer for a bbq and the "Regional Forum Digest" article.

Political

Sans Serif

• Space for pictures - uploaded below.

```html
<!DOCTYPE html>
<html lang="en">
<head>
<meta charset="utf-8">
<title>Member Newsletter</title>
<link rel="stylesheet" href="https://fonts.googleapis.com/css2?family=Arimo:ital,wght@0,400;0,700;1,700&family=Open+Sans:ital,wght@0,600;0,700;1,700&display=swap">
<style>
  :root {
    --blue: #0d5189;
    --red: #c9302c;
    --paper: #f2f2f2;
    --ink: #1e1e1e;
    --muted: #555555;
    --backdrop: #e6e7e9;
    --photo-dark: #2a2f3a;
    --photo-stage: #1d3f8f;
  }
  * { box-sizing: border-box; margin: 0; padding: 0; }
  html, body { width: 1200px; height: 874px; overflow: hidden; }
  body { background: var(--backdrop); font-family: "Arimo", Arial, sans-serif; color: var(--ink); }

  .newsletter {
    position: absolute; left: 290px; top: 10px;
    width: 620px; height: 854px;
    background: var(--paper);
    display: flex; flex-direction: column;
    box-shadow: 0 2px 12px rgba(0,0,0,.12);
  }
  .top-rule { height: 4px; background: var(--red); margin: 12px 30px 0; }
  .masthead { display: flex; align-items: center; gap: 8px; padding: 8px 44px 6px; }
  .masthead-mark { width: 22px; height: 22px; border-radius: 50%; background: var(--blue); }
  .masthead-name { font-weight: 700; font-size: 13px; color: var(--blue); }

  .dateline { display: flex; align-items: flex-end; gap: 14px; padding: 0 30px; }
  .dateline-red { flex: 1; height: 8px; background: var(--red); }
  .dateline-blue { flex: 1; position: relative; height: 8px; background: var(--blue); }
  .dateline-date { position: absolute; right: 10px; bottom: 10px; font-size: 8px; font-weight: 700; color: var(--blue); }

  .photo { display: block; }
  .photo-lead {
    width: 470px; height: 150px; margin: 14px auto 0;
    background: linear-gradient(135deg, #7b6a58 0%, #3d3a3c 55%, #b9b6ae 100%);
  }
  .caption {
    font-family: "Open Sans", Arial, sans-serif; font-weight: 600;
    font-size: 7.5px; line-height: 1.35; text-transform: uppercase; color: var(--muted);
  }
  .caption-lead { text-align: center; width: 260px; margin: 5px auto 0; }

  .article { padding: 0 62px; }
  .article-title { font-size: 15px; font-weight: 700; text-align: center; margin: 10px 0 8px; }
  .article p { font-size: 11.5px; line-height: 1.42; margin-bottom: 8px; }
  .signoff { text-align: right; font-style: italic; font-weight: 700; font-size: 12px; line-height: 1.35; }
  .signoff-email { color: var(--red); }

  .gallery { display: flex; justify-content: center; gap: 22px; margin-top: 12px; }
  .gallery figure { width: 236px; }
  .photo-delegates { height: 112px; background: linear-gradient(160deg, #1f3a8a 0%, var(--photo-dark) 45%, #6d6a66 100%); }
  .photo-stage { height: 112px; background: radial-gradient(ellipse at 60% 40%, #3b6fd6 0%, var(--photo-stage) 45%, #0e1426 100%); }
  .gallery .caption { margin-top: 5px; }

  .cta { text-align: center; font-family: "Open Sans", Arial, sans-serif; font-style: italic; font-weight: 700; margin-top: 14px; }
  .cta-visit { font-size: 12px; color: var(--blue); letter-spacing: .3px; }
  .cta-button { display: inline-block; background: var(--red); color: #fff; font-size: 10.5px; padding: 5px 18px; margin: 4px 0; }
  .cta-call { font-size: 12px; color: var(--red); letter-spacing: .4px; }

  .social { display: flex; justify-content: space-between; align-items: center; padding: 12px 44px 8px; }
  .social-item { display: flex; align-items: center; gap: 6px; font-family: "Open Sans", Arial, sans-serif; font-weight: 600; font-size: 11px; color: var(--blue); }
  .social-dot { width: 16px; height: 16px; border-radius: 50%; background: var(--blue); }

  .footer { margin-top: auto; background: var(--blue); color: #fff; display: flex; justify-content: space-between; padding: 14px 44px; font-size: 10.5px; line-height: 1.45; }
  .footer-contact { text-align: right; }
  .footer-legal { font-size: 9px; }
  .bottom-rule { height: 12px; background: var(--red); }
</style>
</head>
<body>
  <main class="newsletter">
    <div class="top-rule"></div>
    <header class="masthead">
      <span class="masthead-mark"></span>
      <span class="masthead-name">Prairie Heritage Party</span>
    </header>
    <div class="dateline">
      <div class="dateline-red"></div>
      <div class="dateline-blue"><span class="dateline-date">Saturday July 23, 2016</span></div>
    </div>

    <figure>
      <div class="photo photo-lead" role="img" aria-label="Photo of three members at the annual general meeting"></div>
      <figcaption class="caption caption-lead">Hon. Gordon Hale, PC along with R.T. Vance and Peter Coyle at the Heritage AGM in Vancouver</figcaption>
    </figure>

    <article class="article">
      <h1 class="article-title">Regional Forum Digest: Daniel Marchetti</h1>
      <p>It's my pleasure to introduce myself as the newest member of Council from Alberta. I will join Karen Osei from Ridgeford representing the views of members from across the province. I've met many of you over the years, in particular during my three years as EDA President in Northfield Centre, and I'm looking forward to working for you again.</p>
      <p>Over the coming months I will report back on the work of Council, including planning for the next convention, our fundraising goals and the policy process. Please reach out with your questions and ideas at any time. Together we can make sure that the voice of our members is heard and that we bring better government back to our great country.</p>
      <div class="signoff">
        Daniel Marchetti<br>
        Regional Council<br>
        <span class="signoff-email">danielmarchetti@heritageparty.ca</span>
      </div>
    </article>

    <section class="gallery">
      <figure>
        <div class="photo photo-delegates" role="img" aria-label="Photo of delegates seated at convention tables"></div>
        <figcaption class="caption">Northfield Centre delegates working hard at the convention.</figcaption>
      </figure>
      <figure>
        <div class="photo photo-stage" role="img" aria-label="Photo of a large convention hall with a speaker on a blue-lit stage"></div>
        <figcaption class="caption">Thousands gathered as Hon. Helen Ashby, interim leader, addresses the delegates.</figcaption>
      </figure>
    </section>

    <section class="cta">
      <div class="cta-visit">VISIT WWW.HERITAGEPARTY.CA TO</div>
      <div class="cta-button">RENEW YOUR MEMBERSHIP TODAY!</div>
      <div class="cta-call">OR CALL US AT 780-555-0180</div>
    </section>

    <nav class="social">
      <span class="social-item"><span class="social-dot"></span>@NorthfieldHPA</span>
      <span class="social-item"><span class="social-dot"></span>Northfield Centre Heritage Association</span>
    </nav>

    <footer class="footer">
      <address class="footer-address" style="font-style:normal">
        Northern Area Office<br>
        #210, 4400 Prairie Rd NW<br>
        Northfield, AB T0X 0X0<br>
        <span class="footer-legal">This is E-mail 2016. All Rights Reserved.</span>
      </address>
      <div class="footer-contact">
        Phone: 587-555-0134<br>
        780-555-0180<br>
        Fax: 866-555-0107<br>
        E-mail: info@heritageparty.ca
      </div>
    </footer>
    <div class="bottom-rule"></div>
  </main>
</body>
</html>
```